Business card for a "family office" company

Please provide professional looking business card designs, incorporating the attached logo and below details. Harrowmere Holdings Pty Ltd is a family office / financial investment company. We are looking for a modern, professional and contemporary card design.

Industry/Entity Type

Finance

Contact Information for Business Card

Name: Dean Mollick
Title: Director
Company: Harrowmere Holdings Pty Ltd
Email: harrowdean@quillnet.example
Mobile: 0462 735 418
Address: 4/312 Barnaby Parade, Fernhallow QX 7042, Australia

Requirements
Must have
• All details above and the logo. logo only on back side. incorporate colours of logo
Nice to have
• up to you
Should not have
• ?

```html
<!DOCTYPE html>
<html lang="en">
<head>
<meta charset="utf-8">
<title>Harrowmere Holdings – Business Card</title>
<link rel="stylesheet" href="https://fonts.googleapis.com/css2?family=Gelasio:wght@400&display=swap">
<style>
  :root {
    --navy: #1f1f52;
    --navy-text: #24245c;
    --title-blue: #3a3c9c;
    --ink: #2a2a60;
    --paper-light: #f4f4f4;
    --paper-mid: #dcdcdc;
    --paper-shade: #c9c9c9;
    --gap: #ffffff;
    --white: #ffffff;
  }
  * { box-sizing: border-box; margin: 0; padding: 0; }
  html, body {
    width: 1200px;
    height: 329px;
    overflow: hidden;
    background: var(--gap);
    font-family: "Gelasio", Georgia, serif;
  }
  .sheet { position: relative; width: 1200px; height: 329px; }

  .card { position: absolute; top: 0; height: 329px; overflow: hidden; }

  /* Front */
  .card--front {
    left: 0;
    width: 571px;
    background:
      radial-gradient(ellipse 260px 120px at 150px 300px, rgba(180,180,180,.55), transparent 70%),
      linear-gradient(160deg, var(--paper-light) 0%, #ececec 35%, var(--paper-mid) 60%, var(--paper-shade) 75%, #e6e6e6 90%, var(--paper-light) 100%);
  }
  .brand {
    position: absolute;
    left: 0; right: 0;
    top: 34px;
    display: flex;
    flex-direction: column;
    align-items: center;
    gap: 12px;
  }
  .brand__mark {
    width: 62px; height: 62px;
    background: var(--navy-text);
  }
  .brand__name {
    font-size: 26px;
    line-height: 30px;
    font-weight: 400;
    letter-spacing: 1.5px;
    color: var(--navy-text);
    white-space: nowrap;
  }

  .contact {
    position: absolute;
    right: 290px;
    top: 196px;
    text-align: right;
    color: var(--ink);
  }
  .contact__company { font-size: 15px; line-height: 18px; margin-bottom: 5px; }
  .contact__address { font-size: 12.5px; line-height: 18px; }
  .contact__line {
    display: flex;
    justify-content: flex-end;
    align-items: center;
    gap: 7px;
    font-size: 11.5px;
    margin-top: 4px;
  }
  .contact__line svg { display: block; }

  .divider {
    position: absolute;
    left: 289px;
    top: 195px;
    width: 2px;
    height: 92px;
    background: var(--navy-text);
  }
  .person {
    position: absolute;
    left: 298px;
    top: 208px;
    color: var(--navy-text);
  }
  .person__name { font-size: 38px; line-height: 42px; white-space: nowrap; }
  .person__title { font-size: 26px; line-height: 28px; color: var(--title-blue); }

  /* Back */
  .card--back {
    left: 628px;
    width: 572px;
    background: var(--navy);
  }
  .brand--back { top: 93px; gap: 18px; }
  .brand--back .brand__mark { width: 78px; height: 78px; background: var(--white); }
  .brand--back .brand__name { color: var(--white); font-size: 32px; line-height: 36px; letter-spacing: 2px; }
</style>
</head>
<body>
<main class="sheet">
  <section class="card card--front" aria-label="Business card front">
    <div class="brand">
      <span class="brand__mark" aria-hidden="true"></span>
      <span class="brand__name">Harrowmere Holdings</span>
    </div>

    <div class="contact">
      <p class="contact__company">Harrowmere Holdings Pty Ltd.</p>
      <p class="contact__address">4/312 Barnaby Parade, Fernhallow<br>QX 7042, Australia.</p>
      <p class="contact__line">
        <svg width="17" height="17" viewBox="0 0 17 17" aria-hidden="true">
          <circle cx="8.5" cy="8.5" r="8.5" fill="var(--navy-text)"/>
          <path d="M5.6 4.3l1.6-.3.9 2.2-1 .8c.5 1.1 1.3 2 2.4 2.5l.8-1 2.2.9-.3 1.6c-3.6.4-6.9-2.9-6.6-6.7z" fill="#fff"/>
        </svg>
        <span>0462 735 418</span>
      </p>
      <p class="contact__line">
        <svg width="18" height="13" viewBox="0 0 18 13" aria-hidden="true">
          <rect width="18" height="13" rx="1" fill="var(--navy-text)"/>
          <path d="M1.5 1.5l7.5 6 7.5-6M1.5 11.5l5-4.5M16.5 11.5l-5-4.5" stroke="#fff" stroke-width="1.1" fill="none"/>
        </svg>
        <span>harrowdean@quillnet.example</span>
      </p>
    </div>

    <span class="divider" aria-hidden="true"></span>

    <div class="person">
      <p class="person__name">Dean Mollick</p>
      <p class="person__title">Director</p>
    </div>
  </section>

  <section class="card card--back" aria-label="Business card back">
    <div class="brand brand--back">
      <span class="brand__mark" aria-hidden="true"></span>
      <span class="brand__name">Harrowmere Holdings</span>
    </div>
  </section>
</main>
</body>
</html>
```